Medical Internet Marketing Company Needs a Site!

We need a new, fresh website for our search engine optimization and social media marketing company. We specialize in helping medical practices, doctors, physicians, and hospitals with their online presence and web ranking. The site should lean towards being suited for these audiences.

We have several examples of website that we like as well as things that we like about them.

Here are sites that we enjoy.

www.brightwavelab.com

It's a good design for the site all around. The videos, buttons, and images are all excellent. They did a fine job.

- We really like their "contact us" side bar and want to include one like it on the secondary pages.

www.corvantis.net

- We don't like the "thickness" of the top navigation bar.
- We like the page colors, easy navigation, and big call to action phone number in the top right corner.

http://www.teluvo.com/

Out of all the examples provided, Teluvo is our favorite and closest look and style to what we are looking for.

- We really like the openness of the design, such as space between the text and background.

- We want a price page in a style very similar to their pricing page with the services listed and check-marks, etc. although we intend to have multiple service package columns much like Corvantis's SEO pricing page.

- The way the video fits into the home page header is very organized, simple, and attention grabbing. We intend to place a slider with videos here.

- We need a page design that will allow for an image slider like Teluvo's Features page.

Here's a great example of a medical internet marketing website: http://www.dermaplex.com/

Target Market(s)

Our target market is doctors, typically male and typically 40-45 years old. I

Industry/Entity Type

Marketing

Requirements
Must have
• The homepage should have a slider in the video. Interior pages should have a video in the very top similar to how they do it on www.brightwavelab.com

The top navigation tabs needed are:
- Home
- Solutions
- Resources
- About
- Why Quelvo
- Contact

The sidebar should have a GREAT call to action in it on interior pages.

There should be one interior page that is similar to this - http://www.teluvo.com/pricing/

There needs to be a page with multiple boxes that take up a row of the web page's body. This page will house all the case studies similar to brightwave lab's: http://www.brightwavelab.com/success-stories/case-studies/ The one exception is we want the case studies to be inside of "boxes" instead of between horizontal lines like brightwave lab's.
Nice to have
• Color, professional, and clean. GREAT use of calls to actions.

```html
<!DOCTYPE html>
<html lang="en">
<head>
<meta charset="utf-8">
<title>Quelvo – Internet Marketing for Medical Practices</title>
<link rel="stylesheet" href="https://fonts.googleapis.com/css2?family=Arimo:wght@400;700&family=PT+Sans+Narrow:wght@400;700&display=swap">
<style>
:root{
  --blue:#3f97d6;
  --blue-dark:#2a78b8;
  --blue-light:#6fb6e8;
  --green:#7ab83a;
  --green-dark:#5a9a22;
  --orange:#f0901e;
  --orange-dark:#d9740c;
  --nav:#2f2f2f;
  --text:#333;
  --muted:#666;
  --line:#d8d8d8;
  --panel:#f3f3f3;
  --footer:#ececec;
  --white:#fff;
}
*{box-sizing:border-box;margin:0;padding:0}
html,body{width:889px;height:1200px;overflow:hidden}
body{position:relative;background:var(--white);font-family:"Arimo",Arial,sans-serif;color:var(--text);font-size:10.5px}
.abs{position:absolute}
.narrow{font-family:"PT Sans Narrow","Arial Narrow",sans-serif}

/* header */
.brand{left:91px;top:22px;display:flex;align-items:center;gap:10px}
.brand-mark{width:34px;height:34px;background:var(--blue-light)}
.brand-name{font-family:"Arimo",Arial,sans-serif;font-size:38px;font-weight:400;letter-spacing:3px;color:#8a8a8a;line-height:1}
.call{right:112px;top:22px;text-align:right;font-size:9.5px;font-weight:700;color:#666}
.call span{color:var(--green)}
.call-phone{right:112px;top:36px;display:flex;align-items:center;gap:6px;font-size:21px;font-weight:700;color:var(--green)}

/* nav */
.nav{left:91px;top:80px;width:706px;height:29px;background:linear-gradient(#3a3a3a,#222);border-radius:3px;display:flex;align-items:stretch}
.nav a{color:var(--white);text-decoration:none;font-size:10px;font-weight:700;text-transform:uppercase;display:flex;align-items:center;padding:0 20px;border-right:1px solid #444}
.nav a.active{background:linear-gradient(#9ad154,var(--green-dark));color:#222}
.login{right:20px;top:5px;height:19px;padding:0 26px 0 12px;background:linear-gradient(var(--blue-light),var(--blue-dark));border-radius:3px;color:var(--white);font-size:9px;font-weight:700;display:flex;align-items:center}
.login svg{position:absolute;right:6px;top:3px}

/* hero */
.hero{left:91px;top:131px;width:706px;height:200px;background:linear-gradient(90deg,#eef1f3,#f7f7f7);border-radius:4px}
.hero-title{left:21px;top:20px;font-size:26px;font-weight:700;color:var(--blue);line-height:31px}
.hero-sub{left:21px;top:89px;font-size:25px;color:var(--blue);font-family:"Arimo",Arial,sans-serif}
.hero-list{left:21px;top:123px;list-style:none}
.hero-list li{font-size:12.5px;font-weight:700;line-height:20px;color:#222;padding-left:14px;position:relative}
.hero-list li::before{content:"";position:absolute;left:0;top:6px;border:4px solid transparent;border-left:5px solid var(--green)}
.watch{left:290px;top:93px;width:88px;height:26px;border-radius:13px;background:linear-gradient(#9ad154,var(--green-dark));color:var(--white);font-size:12px;display:flex;align-items:center;justify-content:center;gap:5px}
.hero-photo{left:378px;top:12px;width:314px;height:180px;background:linear-gradient(120deg,#f5f7f9,#dfe6ec 60%,#c6d6e3);border:3px solid var(--white);box-shadow:0 1px 4px rgba(0,0,0,.25)}

/* services */
.services{left:91px;top:351px;width:706px;height:502px;background:linear-gradient(#fafafa,#f0f0f0);border:1px solid var(--line);border-radius:4px}
.svc-head{top:0;height:52px;background:linear-gradient(var(--blue-light),var(--blue));color:var(--white);font-size:20px;font-weight:700;text-transform:uppercase;padding:13px 0 0 20px}
.svc-img{width:108px;height:95px;border:3px solid var(--white);box-shadow:0 1px 4px rgba(0,0,0,.25)}
.svc-text{width:190px;font-size:10.6px;line-height:16px;color:#333}
.btn-orange{height:18px;padding:0 8px;background:linear-gradient(#f6a84a,var(--orange));color:var(--white);font-size:9.5px;font-weight:700;display:flex;align-items:center;border-radius:2px}

/* columns */
.col-head{height:21px;display:flex;align-items:center;gap:6px}
.col-head i{width:24px;height:21px;background:var(--blue-light);display:block}
.col-head b{flex:1;height:21px;background:linear-gradient(var(--blue-light),var(--blue));color:var(--white);font-size:15px;padding:2px 8px;text-transform:uppercase}
.col-img{width:185px;height:77px;border:2px solid var(--white);box-shadow:0 1px 3px rgba(0,0,0,.25)}
.col-text{width:195px;font-size:10px;line-height:13.5px;color:#333}
.pill{height:18px;padding:0 24px 0 8px;border:1px solid #ccc;border-radius:9px;background:var(--white);color:var(--orange-dark);font-size:9px;font-weight:700;display:flex;align-items:center}
.pill::after{content:"»";position:absolute;right:4px;top:2px;width:12px;height:12px;border-radius:50%;background:var(--orange);color:var(--white);font-size:9px;line-height:11px;text-align:center}
.quick-call{left:597px;top:608px;font-size:10.5px;font-weight:700;color:var(--blue-dark);line-height:16px}
.quick-call span{font-size:16px;color:var(--blue)}
.field{left:591px;width:184px;height:19px;border:1px solid #ccc;background:var(--white);font-size:8.5px;font-style:italic;color:#999;padding:4px 5px;border-radius:2px}

/* band */
.band-text{left:112px;top:885px;font-size:18px;line-height:20px;color:#555}
.band-text b{color:var(--blue)}
.band-btn{left:112px;top:953px;width:208px;height:24px;background:linear-gradient(#8fc94a,var(--green-dark));color:var(--white);font-size:14px;font-weight:700;display:flex;align-items:center;justify-content:center}
.carousel{left:377px;top:880px;width:379px;height:104px;background:var(--panel);border:1px solid #e3e3e3}
.car-item{top:8px;width:120px;text-align:center;font-size:9.5px;font-weight:700;color:#222}
.car-art{margin:10px auto 0;width:56px;height:56px}

/* footer */
.footer{left:0;top:1000px;width:889px;height:200px;background:var(--footer)}
.foot-panel{left:91px;top:1009px;width:706px;height:140px;background:var(--white);border-radius:3px;box-shadow:0 2px 4px rgba(0,0,0,.08)}
.foot-col{top:1023px}
.foot-col h4{font-size:9px;font-weight:700;color:var(--orange);text-transform:uppercase;padding-bottom:4px;border-bottom:1px dotted #bbb;margin-bottom:4px;width:84px}
.foot-col li{list-style:none;font-size:8.8px;color:#444;line-height:17px;padding-left:12px;position:relative}
.foot-col li::before{content:"";position:absolute;left:0;top:6px;border:3px solid transparent;border-left:4px solid #333}
.foot-col.social li::before{border:0;width:7px;height:7px;border-radius:50%;background:#888;top:5px}
.foot-brand{left:613px;top:1027px;display:flex;align-items:center;gap:6px}
.foot-brand i{width:18px;height:18px;background:var(--blue-light);display:block}
.foot-brand b{font-size:20px;font-weight:400;letter-spacing:2px;color:#8a8a8a}
.foot-addr{left:653px;top:1056px;font-size:8.5px;line-height:13px;color:#444}
.foot-addr span{color:var(--blue)}
.foot-links{left:119px;top:1164px;font-size:8px;color:#333}
.foot-copy{left:119px;top:1179px;font-size:8px;color:#333}
.foot-credit{left:649px;top:1164px;font-size:8px;color:#333}
</style>
</head>
<body>

<header>
  <div class="abs brand"><span class="brand-mark"></span><span class="brand-name">QUELVO</span></div>
  <div class="abs call">Have a question? <span>Give us a CALL</span></div>
  <div class="abs call-phone">
    <svg width="12" height="16" viewBox="0 0 12 16"><rect x="1" y="1" width="10" height="14" rx="2" fill="none" stroke="#999" stroke-width="1.5"/><rect x="3" y="3" width="6" height="8" fill="#bbb"/></svg>
    <svg width="7" height="10" viewBox="0 0 7 10"><path d="M1 1l5 4-5 4z" fill="#7ab83a"/></svg>
    0198-765-432
  </div>
  <nav class="abs nav">
    <a class="active">Home</a><a>Solutions</a><a>Resources</a><a>About</a><a>Why Quelvo</a><a>Contact</a>
    <span class="abs login">MEMBERS LOGIN
      <svg width="14" height="13" viewBox="0 0 14 13"><circle cx="7" cy="4" r="3.2" fill="#1c2e40"/><path d="M1 13c0-4 3-6 6-6s6 2 6 6z" fill="#1c2e40"/></svg>
    </span>
  </nav>
</header>

<section class="abs hero">
  <h1 class="abs hero-title narrow">Internet Marketing &amp; Websites for<br>Medical Practices</h1>
  <p class="abs hero-sub">Be Found Online</p>
  <ul class="abs hero-list">
    <li>Attract More Website Visiors</li>
    <li>Target High Value Patients</li>
    <li>Master Social Media Opportunities</li>
  </ul>
  <div class="abs watch">Watch Video
    <svg width="7" height="10" viewBox="0 0 7 10"><path d="M1 1l4 4-4 4" stroke="#fff" stroke-width="2" fill="none"/></svg>
  </div>
  <div class="abs hero-photo" role="img" aria-label="Doctor in a white coat holding a tablet against a backdrop of marketing keywords"></div>
</section>

<main class="abs services">
  <h2 class="abs svc-head narrow" style="left:0;width:353px">Search Engine Optimization</h2>
  <h2 class="abs svc-head narrow" style="left:353px;width:353px;border-left:1px solid #8cc3ea">Social Media Marketing</h2>

  <div class="abs svc-img" style="left:21px;top:70px;background:radial-gradient(circle at 40% 50%,#5aa6e6,#1f5fa8 55%,#e9eef3 56%)" role="img" aria-label="Glossy SEO lettering under a magnifying glass"></div>
  <p class="abs svc-text" style="left:141px;top:70px">QUELVO offers a complete Search Engine Marketing (SEM) program that combines the best features of traditional Search Engine Optimization (SEO) and cutting-edge Pay-Per-Click ad campaign management to ensure your success.</p>
  <span class="abs btn-orange" style="left:141px;top:178px">Get a Free Trial Today &nbsp;»</span>

  <div class="abs svc-img" style="left:376px;top:70px;background:radial-gradient(circle,#f2c14a,#6bbf4a 45%,#e45a3b 70%,#f2f2f2 72%)" role="img" aria-label="Cluster of colourful social media speech bubbles"></div>
  <p class="abs svc-text" style="left:496px;top:70px">QUELVO offers a complete Search Engine Marketing (SEM) program that combines the best features of traditional Search EngineOptimization (SEO) and cutting-edge Pay-Per-Click ad campaign management to ensure your success.</p>
  <span class="abs btn-orange" style="left:499px;top:178px">Get a Free Trial Today &nbsp;»</span>
</main>

<section>
  <div class="abs col-head narrow" style="left:112px;top:577px;width:185px"><i></i><b>About Quelvo</b></div>
  <div class="abs col-img" style="left:112px;top:607px;background:linear-gradient(#e8eef4,#b9c9d8)" role="img" aria-label="The word optimization over rows of binary digits"></div>
  <div class="abs col-text" style="left:112px;top:696px">We are the premier communications company specializing in helping healthcare organizations acquire, engage + succeed in the digital age.<br><br>Each website we create is powered by our exclusive SiteForge Technology, giving you unmatched advantages that save you time and money.</div>
  <span class="abs pill" style="left:109px;top:819px">Know More About Us</span>

  <div class="abs col-head narrow" style="left:352px;top:577px;width:185px"><i></i><b>Why Us</b></div>
  <div class="abs col-img" style="left:352px;top:607px;background:linear-gradient(90deg,#fafafa,#e3ecf4)" role="img" aria-label="Hand drawing an SEO diagram with design, html, keywords and backlinks on a whiteboard"></div>
  <div class="abs col-text" style="left:352px;top:696px"><b>SEO is the factor takes a website design and propels it to a powerful marketing device.</b><br><br>SEO is our core focus, and our core competency. In our design cycle we generally spend from between 55 to 60% of our efforts on SEO.</div>
  <span class="abs pill" style="left:347px;top:819px">Sign Up Today &amp; Get Started</span>

  <div class="abs col-head narrow" style="left:591px;top:577px;width:186px"><i></i><b>Quick Contact</b></div>
  <p class="abs quick-call">CALL US on <span>001-876-5432</span> OR<br>drop us a line by filling this form</p>
  <div class="abs field" style="top:647px">enter your name</div>
  <div class="abs field" style="top:673px">enter your email</div>
  <div class="abs field" style="top:700px">enter your phone #</div>
  <div class="abs field" style="top:727px;height:68px">message</div>
  <span class="abs pill" style="left:596px;top:819px">Submit</span>
</section>

<section>
  <p class="abs band-text narrow">Get A Behind-the-scenes Look At What<br>Makes <b>QUELVO</b> The Ultimate Website<br>Solution For Your Practice.</p>
  <div class="abs band-btn narrow">Medical Websites Service Solutions</div>
  <svg class="abs" style="left:343px;top:910px" width="26" height="44" viewBox="0 0 26 44"><path d="M22 2L4 22l18 20" stroke="#c8c8c8" stroke-width="4" fill="none"/></svg>
  <svg class="abs" style="left:770px;top:910px" width="26" height="44" viewBox="0 0 26 44"><path d="M4 2l18 20L4 42" stroke="#c8c8c8" stroke-width="4" fill="none"/></svg>
  <div class="abs carousel">
    <div class="abs car-item" style="left:4px">Website Analytics
      <div class="car-art" style="background:linear-gradient(#4a8fd0,#dfe8f1)" role="img" aria-label="Browser window with analytics charts"></div></div>
    <div class="abs car-item" style="left:129px">Local Search Marketing
      <div class="car-art" style="width:70px;height:50px;margin-top:14px;background:#e2e2e2;border-radius:4px" role="img" aria-label="Qualified partner badge"></div></div>
    <div class="abs car-item" style="left:254px">Social Media &amp; Blogs
      <div class="car-art" style="background:radial-gradient(circle,#f18c2d 40%,#3a86c8 41%,#3a86c8 60%,transparent 62%)" role="img" aria-label="Social media icons"></div></div>
  </div>
</section>

<footer>
  <div class="abs footer"></div>
  <div class="abs foot-panel"></div>
  <div class="abs foot-col" style="left:117px"><h4>About Quelvo</h4><ul><li>Home</li><li>Solutions</li><li>Resources</li><li>About</li><li>Why Quelvo</li><li>Contact</li></ul></div>
  <div class="abs foot-col" style="left:228px"><h4>Solutions</h4><ul><li>Search Engine Optimization</li><li>Social Media Marketing</li><li>Web Analytics</li><li>Data Management</li><li>Online Marketing</li><li>Advertising</li></ul></div>
  <div class="abs foot-col" style="left:369px"><h4>Expertise</h4><ul><li>Paid Search Ads</li><li>Webinars</li><li>Guides</li><li>Events</li><li>Training</li></ul></div>
  <div class="abs foot-col social" style="left:488px"><h4>Follow Us</h4><ul><li>RSS</li><li>Seekora</li><li>Chatterly</li><li>Circlebook</li></ul></div>
  <div class="abs foot-brand"><i></i><b>QUELVO</b></div>
  <p class="abs foot-addr">2750 Harbor Lane, Suite 410<br>Lakeview Heights, NY 10960<br><br><b>Tel:</b> +1 (198) 765-43210<br><b>Email:</b> <span>info@quelvo.com</span></p>
  <p class="abs foot-links">Contacts &nbsp;|&nbsp; Help &nbsp;|&nbsp; Sitemap &nbsp;|&nbsp; Terms &amp;Conditions &nbsp;|&nbsp; Privacy &nbsp;Statement</p>
  <p class="abs foot-copy">© 2012, &nbsp;Quelvo &nbsp;|&nbsp; All Rights Reserved</p>
  <p class="abs foot-credit">Website Design &amp; Developed By</p>
</footer>

</body>
</html>
```